Stationery Design Project

We need a stationery design for a new business consulting business based in New Zealand.
We have the logo and business cards designed and we're looking for letterhead, compliments slip and PowerPoint presentation format that aligns with our business cards.
Industry/Entity Type
Business
Requirements
Must have
- same colors and format as business cards

```html
<!DOCTYPE html>
<html lang="en">
<head>
<meta charset="utf-8">
<title>Kauri Advisory – Presentation Template</title>
<link rel="stylesheet" href="https://fonts.googleapis.com/css2?family=Arimo:wght@400;700&family=Carlito:wght@400;700&family=Questrial&display=swap">
<style>
  :root {
    --stage: #56605f;
    --lime: #86f51c;
    --slate: #9aa2a2;
    --ink: #3d4242;
    --ink-soft: #4f5555;
    --muted: #a3a8a8;
    --paper: #ffffff;
  }
  * { margin: 0; padding: 0; box-sizing: border-box; }
  html, body { width: 1200px; height: 1200px; overflow: hidden; }
  body {
    background: var(--stage);
    font-family: "Carlito", "Calibri", sans-serif;
    color: var(--ink);
    position: relative;
  }
  .slide {
    position: absolute;
    width: 562px;
    height: 420px;
    background: var(--paper);
    overflow: hidden;
    box-shadow: 0 2px 6px rgba(0,0,0,.35);
  }
  .slide--cover { left: 23px; top: 173px; background: linear-gradient(180deg, #f6f7f7 0%, #e4e7e7 100%); }
  .slide--strategy { left: 612px; top: 173px; }
  .slide--definitions { left: 23px; top: 627px; }
  .slide--closing { left: 612px; top: 627px; background: linear-gradient(180deg, #f7f8f8 0%, #e6e9e9 100%); }

  .band-top { position: absolute; left: 266px; top: 0; width: 296px; height: 45px; background: var(--lime); }
  .band { position: absolute; background: var(--lime); }
  .strip { position: absolute; background: var(--slate); }
  .photo { position: absolute; z-index: 0; }

  .brand {
    position: absolute;
    left: 40px;
    display: flex;
    align-items: center;
    gap: 8px;
    font-family: "Arimo", sans-serif;
    font-weight: 400;
    font-size: 29px;
    letter-spacing: -0.5px;
    color: var(--muted);
    white-space: nowrap;
  }
  .brand__mark { width: 13px; height: 13px; background: var(--lime); }

  .slide-title {
    position: absolute;
    font-family: "Arimo", sans-serif;
    font-size: 23px;
    font-weight: 400;
    color: var(--ink-soft);
  }
  .cover-title {
    position: absolute;
    left: 0; right: 0; top: 128px;
    text-align: center;
    font-family: "Arimo", sans-serif;
    font-weight: 700;
    font-size: 22px;
    color: var(--ink);
  }

  .bullets {
    position: absolute;
    z-index: 2;
    list-style: none;
    font-size: 14px;
    line-height: 19px;
    color: var(--ink-soft);
  }
  .bullets li { position: relative; padding-left: 19px; margin-bottom: 20px; }
  .bullets li::before { content: "•"; position: absolute; left: 0; top: 0; font-size: 11px; }
  .sub-list { list-style: none; margin-top: 21px; }
  .sub-list li { padding-left: 0; margin-bottom: 0; line-height: 20px; }
  .sub-list li::before { content: none; }

  .contact {
    position: absolute; left: 264px; top: 50px;
    font-family: "Questrial", sans-serif;
    font-style: normal;
    font-size: 10.5px; line-height: 14px;
    color: var(--muted);
  }
  .contact p { display: flex; align-items: center; gap: 5px; font-weight: 700; }
  .contact svg { width: 9px; height: 9px; flex: none; }

  .thanks {
    position: absolute; left: 60px; top: 145px;
    font-family: "Arimo", sans-serif;
    font-size: 22px;
    font-weight: 400;
    color: var(--ink-soft);
  }
</style>
</head>
<body>

  <section class="slide slide--cover">
    <div class="band-top"></div>
    <div class="brand" style="top:58px"><span class="brand__mark"></span>Kauri Advisory</div>
    <h1 class="cover-title">INTRODUCTION TO STRATEGY</h1>
    <div class="photo" role="img" aria-label="Chess piece on a dark board" style="left:514px;top:45px;width:48px;height:170px;background:linear-gradient(180deg,#c9d2dc,#3a4350);"></div>
    <div class="band" style="left:0;top:215px;width:352px;height:57px;"></div>
    <div class="photo" role="img" aria-label="Flowchart of strategy steps on paper with a pen" style="left:354px;top:215px;width:160px;height:57px;background:linear-gradient(135deg,#e9eef3,#7fa6cc);"></div>
    <div class="strip" style="left:0;top:272px;width:42px;height:118px;"></div>
    <div class="photo" role="img" aria-label="Boardroom chairs on a reflective floor under a blue sky" style="left:42px;top:272px;width:472px;height:118px;background:linear-gradient(180deg,#8fb4d8 0%,#dfe9f2 55%,#3b3f44 80%,#cfd6dc 100%);"></div>
    <div class="strip" style="left:514px;top:272px;width:48px;height:118px;"></div>
    <div class="band" style="left:0;top:390px;width:562px;height:30px;"></div>
  </section>

  <section class="slide slide--strategy">
    <div class="band-top"></div>
    <div class="brand" style="top:23px"><span class="brand__mark"></span>Kauri Advisory</div>
    <h2 class="slide-title" style="left:60px;top:73px;">Strategy</h2>
    <ul class="bullets" style="left:37px;top:124px;width:230px;">
      <li>An organizations strategy shows what the organisation wants to achieve and how it will achieve it</li>
    </ul>
    <ul class="bullets" style="left:297px;top:124px;width:250px;">
      <li>It includes:
        <ul class="sub-list">
          <li>-The purpose of the organisation</li>
          <li>-Goals and objectives</li>
          <li>-Plans and methods to achieve<br>&nbsp;these goals and objectives</li>
        </ul>
      </li>
    </ul>
    <div class="strip" style="left:0;top:270px;width:42px;height:150px;"></div>
    <div class="photo" role="img" aria-label="Keyboard with a blue success key" style="left:42px;top:270px;width:141px;height:150px;background:linear-gradient(135deg,#d3d7da 0%,#8a9096 45%,#3e9be0 70%,#5a6066 100%);"></div>
  </section>

  <section class="slide slide--definitions">
    <div class="band-top"></div>
    <div class="brand" style="top:13px"><span class="brand__mark"></span>Kauri Advisory</div>
    <h2 class="slide-title" style="left:62px;top:70px;">Some definitions of strategy</h2>
    <ul class="bullets" style="left:37px;top:124px;width:240px;">
      <li>A proposed action or sequence of action intended to have far reaching effects on the organizations ability to achieve ist objectives</li>
    </ul>
    <ul class="bullets" style="left:296px;top:124px;width:245px;">
      <li>A proposed action or sequence of action intended to have far reaching effects on the organizations ability to achieve ist objectives</li>
      <li>A proposed action or sequence of action intended to have far reaching effects on the organizations ability to achieve ist objectives</li>
      <li>A proposed action or sequence of action intended to have far reaching effects.</li>
    </ul>
    <div class="band" style="left:0;top:250px;width:143px;height:18px;"></div>
    <div class="strip" style="left:0;top:268px;width:42px;height:152px;"></div>
    <div class="photo" role="img" aria-label="Businessman pushing a large puzzle piece into place" style="left:42px;top:268px;width:248px;height:152px;background:linear-gradient(90deg,#e8eaeb 0%,#f4f5f5 70%,#ffffff 100%);"></div>
  </section>

  <section class="slide slide--closing">
    <div class="brand" style="top:53px"><span class="brand__mark"></span>Kauri Advisory</div>
    <address class="contact">
      <p>PO Box 48120</p>
      <p>Wellington 6140 New Zealand</p>
      <p><svg viewBox="0 0 10 10"><path d="M2 1l2 0 1 2.5-1.3 1a5 5 0 0 0 2.8 2.8l1-1.3L10 7v2a1 1 0 0 1-1 1A9 9 0 0 1 0 1a1 1 0 0 1 1-1z" fill="var(--lime)"/></svg>+ 64 21555014</p>
      <p><svg viewBox="0 0 10 10"><rect x="0.5" y="2" width="9" height="6.5" fill="none" stroke="var(--lime)"/><path d="M0.5 2l4.5 3.5L9.5 2" fill="none" stroke="var(--lime)"/></svg>hello@kauriadvisory.com</p>
      <p><svg viewBox="0 0 10 10"><circle cx="5" cy="5" r="4.5" fill="var(--lime)"/></svg>www.kauriadvisory.com</p>
    </address>
    <h2 class="thanks">THANK YOU</h2>
    <div class="strip" style="left:0;top:270px;width:42px;height:150px;"></div>
    <div class="photo" role="img" aria-label="Group of five business professionals standing together" style="left:262px;top:232px;width:232px;height:188px;background:linear-gradient(180deg,#4a4f57 0%,#23262b 100%);border-radius:40px 40px 0 0;"></div>
  </section>

</body>
</html>
```